Business card for Cat Cafe

I have started a small business and need a business card designed. The business is a cat cafe, that is, an ordinary cafe that serves coffee and snacks but with a twist - you can bring your cat to play. In fact the idea is to encourage everyone to come and bring your feline friend in order to build community and provide some fun and connections between fellow cat lovers. Themes of the business include;

- Fun
- Discovery
- Connections

The name of the cafe is Brews and Whiskers!

We look forward to seeing what creative ideas you may have!
Updates

Hi,

 Please note the contact details as below;
14 Tarrant Lane, Marlow Vale,
Sydney, NSW
2010

Target Market(s)

Cat owners, any age group

Industry/Entity Type

Small Business

Requirements
Must have
• Must include some type of imagery of a cat itself.

```html
<!DOCTYPE html>
<html lang="en">
<head>
<meta charset="utf-8">
<title>Brews &amp; Whiskers! – Business Card</title>
<link href="https://fonts.googleapis.com/css2?family=Dosis:wght@700;800&family=Nunito+Sans:wght@700&display=swap" rel="stylesheet">
<style>
  :root {
    --page-bg: #ffffff;
    --card-bg: #eceeee;
    --ink-dark: #2b2a29;
    --accent-yellow: #d4db1c;
    --text-light: #ffffff;
    --art-tone: #4a4a47;
    --text-shadow: rgba(60, 60, 40, 0.45);
  }
  html, body {
    margin: 0;
    padding: 0;
    width: 1200px;
    height: 831px;
    overflow: hidden;
    background: var(--page-bg);
  }
  .business-card {
    position: absolute;
    left: 227px;
    top: 193px;
    width: 740px;
    height: 460px;
    border-radius: 28px;
    background: var(--card-bg);
    overflow: hidden;
    box-shadow: 0 10px 22px rgba(0, 0, 0, 0.22);
  }
  .ground-band {
    position: absolute;
    left: 0;
    top: 0;
    width: 740px;
    height: 460px;
  }
  .cafe-name {
    position: absolute;
    left: 44px;
    top: 50px;
    margin: 0;
    font-family: "Dosis", sans-serif;
    font-weight: 800;
    font-size: 50px;
    line-height: 58px;
    color: var(--accent-yellow);
    text-transform: uppercase;
    text-shadow: 1px 2px 2px var(--text-shadow);
    transform: rotate(-4deg);
    transform-origin: left top;
  }
  .cafe-art {
    position: absolute;
    left: 196px;
    top: 14px;
    width: 292px;
    height: 252px;
    background: linear-gradient(180deg, var(--art-tone), var(--ink-dark));
    border-radius: 10px;
  }
  .tagline {
    position: absolute;
    left: 496px;
    top: 92px;
    width: 234px;
    margin: 0;
    font-family: "Dosis", sans-serif;
    font-weight: 800;
    font-size: 40px;
    line-height: 52px;
    color: var(--accent-yellow);
    text-transform: uppercase;
    text-align: center;
    text-shadow: 1px 2px 2px var(--text-shadow);
    transform: rotate(-6deg);
  }
  .address {
    position: absolute;
    left: 0;
    top: 333px;
    width: 740px;
    margin: 0;
    text-align: center;
    font-family: "Nunito Sans", sans-serif;
    font-weight: 700;
    font-size: 22px;
    color: var(--text-light);
  }
  .values {
    position: absolute;
    left: 0;
    top: 386px;
    width: 740px;
    margin: 0;
    padding: 0;
    list-style: none;
    display: flex;
    justify-content: center;
    gap: 14px;
    font-family: "Dosis", sans-serif;
    font-weight: 700;
    font-size: 29px;
    color: var(--accent-yellow);
  }
  .values li + li::before {
    content: "\2022";
    margin-right: 14px;
  }
</style>
</head>
<body>
  <div class="business-card">
    <svg class="ground-band" viewBox="0 0 740 460" aria-hidden="true">
      <polygon fill="var(--accent-yellow)"
        points="0,272 40,270 60,264 120,266 150,258 190,266 260,262 300,268 340,256 380,266 420,260 470,266 500,254 540,262 600,258 640,266 680,256 740,262 740,460 0,460"/>
      <polygon fill="var(--ink-dark)"
        points="0,280 40,278 60,272 120,274 150,266 190,274 260,270 300,276 340,264 380,274 420,268 470,274 500,262 540,270 600,266 640,274 680,264 740,270 740,460 0,460"/>
    </svg>

    <h1 class="cafe-name">Cat<br>Cafe</h1>

    <div class="cafe-art" role="img" aria-label="Illustration of a black cat walking beside a steaming yellow coffee cup"></div>

    <p class="tagline">Brews &amp;<br>Whiskers!</p>

    <p class="address">14 Tarrant Lane, Marlow Vale,&nbsp; Sydney, NSW 2010</p>

    <ul class="values">
      <li>Fun</li>
      <li>Discovery</li>
      <li>Connections</li>
    </ul>
  </div>
</body>
</html>
```